Restaurant Poster Design Project for A-Frame

I am after a poster, which will go on an outdoor A-Frame (A1 size - this size is to be confirmed) outlining our drink/happy hour/specials for our Mexican Restaurant and Bar.

Specific details are:

$4 Beer, Wine and Spirits
$5 Margaritas
everynight 5:30pm-7:30pm

I will supply logo, which needs to be incorporated (really small) into the poster, along with our address: 42 Birchwood Lane, Windsor - (Im not too sure if we should include our phone number or not ?? Please advise what you feel will look good etc

Happy for you to add a phrase or wording etc, as long as the specific details are included, above.

We also have an enclosed beer garden in the rear of the restaurant - Do you believe I should mention this?

I am really open to eye catching designs and ALL suggestions welcome please!
Updates

Please find attached of samples that I am sort of after: (please let me know if they cant be opened).

http://www.flyerwisp.com/blog/wp-content/uploads/2012/06/happyHourPoster-e1340372894746.gif

http://marnelvek.files.pagekiln.com/2012/10/profolio_0012.jpg?w=1169

http://3.cd.notequill.com/-NfNjpdG5w/T5pohPd0AhI/AAAAAAAADRs/CA7DPeI_PyU/s640/vintage_poster.jpg

http://www.quorvanhill.com/files/imagecache/Event/news/teaser/Lounge_Happy_Hour_Poster_-_Mar_2011_bilingual.jpg

http://www.tpelmors.com/dallas/images/happyhour_poster.jpg

http://cdn2-b.newsgarrow.com/sites/default/files/styles/large_lightbox/hash/9a/d1/9ad11350ba178511886fddcff7aaac8d.jpg?itok=wDl2vlfJ

http://www.platefinchly.com/imageservice/images/13/1313171414293_244/img_large_watermarked.jpg

Target Market(s)

18 YEARS OLD AND OVER

Industry/Entity Type

Restaurant

Requirements
Must have
• Address
Phone Number
Logo
Clear easy to read font, to be seen via cars + ppl walking down street
If images are included, to be clear and visable
Nice to have
• Images are possible
To mention a beer garden
Should not have
• Traditional Mexican Colourful 80's Theme

```html
<!DOCTYPE html>
<html lang="en">
<head>
<meta charset="utf-8">
<title>Happy Hour – 42 Birchwood Lane, Windsor</title>
<link rel="stylesheet" href="https://fonts.googleapis.com/css2?family=UnifrakturMaguntia&family=Parisienne&display=swap">
<style>
  :root {
    --paper: #ffffff;
    --pink-light: #ffd6ea;
    --pink-mid: #f48cc0;
    --pink-deep: #c2457f;
    --pink-edge: #9e2f63;
    --lavender: #9c6fe0;
  }
  html, body {
    margin: 0;
    padding: 0;
    overflow: hidden;
    background: var(--paper);
  }
  .poster {
    position: relative;
    width: 1200px;
    height: 300px;
    overflow: hidden;
    background: var(--paper);
  }
  .glass-art {
    position: absolute;
    left: 12px;
    top: 66px;
    width: 100px;
    height: 172px;
  }
  .address {
    position: absolute;
    left: 140px;
    top: 0;
    width: 1056px;
    margin: 0;
    font-family: "UnifrakturMaguntia", serif;
    font-weight: 400;
    font-size: 60px;
    line-height: 76px;
    letter-spacing: 3px;
    word-spacing: 22px;
    white-space: nowrap;
    text-align: right;
    background: linear-gradient(180deg, var(--pink-light) 0%, var(--pink-mid) 55%, var(--pink-deep) 100%);
    -webkit-background-clip: text;
    background-clip: text;
    color: transparent;
    -webkit-text-stroke: 1px var(--pink-edge);
  }
  .offers {
    position: absolute;
    left: 466px;
    top: 112px;
    margin: 0;
    padding: 0;
    list-style: none;
    font-family: "Parisienne", cursive;
    font-size: 33px;
    line-height: 60px;
    color: var(--lavender);
  }
</style>
</head>
<body>
  <main class="poster">
    <svg class="glass-art" viewBox="0 0 100 172" role="img" aria-label="Pink martini glass with an olive">
      <defs>
        <linearGradient id="glassTone" x1="0" y1="0" x2="1" y2="1">
          <stop offset="0" stop-color="#ffc2e0"/>
          <stop offset="1" stop-color="#e0529a"/>
        </linearGradient>
      </defs>
      <rect x="0" y="0" width="100" height="172" fill="url(#glassTone)" opacity="0.55"/>
    </svg>

    <h1 class="address">42 Birchwood Lane, Windsor</h1>

    <ul class="offers">
      <li class="offer">$4 Beer, Wine and Spirits</li>
      <li class="offer">$5 Margaritas</li>
      <li class="offer offer-hours">everynight 5:30pm-7:30pm</li>
    </ul>
  </main>
</body>
</html>
```